Web Design For Metal Recycling Company

We are a scrap and recycling company dealing mainly in scrap metal base in Singapore. We deal in both domestic market and international market. Currently we are still unsure if we want to have a "lively" or "professional" company image so we will leave it to the designer to deem what is good.

We wish for a website to be able to "Retain" the interest of new visitor and at the same time able to give enough information for new and existing customer. We would also wish for design that will get the visitor to "Engage" us.

The attached is the logo for the company and we would want to incorporate that into the website. Either of the logo is fine.

```html
<!DOCTYPE html>
<html lang="en">
<head>
<meta charset="utf-8">
<title>Terra Loop Recycling</title>
<link rel="stylesheet" href="https://fonts.googleapis.com/css2?family=Roboto+Condensed:wght@400;700&family=Roboto:wght@400;700&display=swap">
<style>
:root{
  --gold:#c9962f;
  --gold-deep:#b8861f;
  --gold-light:#f3d58c;
  --cream:#f6e6c0;
  --cream-pale:#fdf1d2;
  --grey:#6c6c6c;
  --grey-light:#efefef;
  --page:#eeeeee;
  --ink:#111111;
  --white:#ffffff;
  --footer:#050505;
}
*{margin:0;padding:0;box-sizing:border-box}
html,body{width:1028px;height:1200px;overflow:hidden;background:var(--page)}
body{position:relative;font-family:"Roboto Condensed",Arial,sans-serif;color:var(--ink)}
.abs{position:absolute}

/* brand */
.brand{left:150px;top:10px;width:140px;text-align:center}
.brand-mark{width:34px;height:34px;border:3px solid var(--gold);margin:0 auto 6px}
.brand-name{font-size:17px;color:var(--gold);letter-spacing:1px;line-height:1}
.brand-sub{font-size:9px;color:var(--gold);letter-spacing:2px;text-align:right;padding-right:10px}

/* nav */
.nav{left:103px;top:92px;width:822px;height:31px;border-radius:6px;
  background:linear-gradient(#f3dea6 0 30%,var(--gold) 30% 100%);display:flex;align-items:center}
.nav a{position:absolute;transform:translateX(-50%);top:9px;font-size:12.5px;font-weight:700;color:var(--ink);text-decoration:none;white-space:nowrap}
.nav a.active{color:var(--white)}

/* hero */
.hero{left:103px;top:131px;width:822px;height:226px;overflow:hidden;
  background:linear-gradient(#fde2a0,#f8e9c8 60%,#e2e2e2)}
.hero-visual{position:absolute;left:337px;top:0;width:485px;height:226px;
  background:radial-gradient(ellipse at 55% 20%,#c9962f 0,#a98a48 22%,rgba(240,210,140,0) 45%),
  linear-gradient(transparent 45%,#9c9c9c 75%,#cfcfcf)}
.hero-title{position:absolute;left:0;top:44px;width:380px;text-align:center;font-weight:700;
  font-size:41px;line-height:51px;color:var(--ink);text-shadow:2px 2px 0 #fff,-1px -1px 0 #fff}

/* steps */
.steps{left:103px;top:357px;width:822px;height:110px}
.step-title{position:absolute;font-weight:700;font-size:15px}
.step-text{position:absolute;font-family:Roboto,Arial,sans-serif;font-size:8.5px;line-height:15px;width:170px;color:#333}
.step-icon{position:absolute;width:58px;height:58px;border-radius:50%;background:var(--white);display:flex;align-items:center;justify-content:center}

/* why */
.why{left:103px;top:477px;width:384px;height:383px;border:2px solid var(--gold);border-radius:10px;background:var(--white);padding:12px 10px}
.frame{border:3px double var(--ink);height:100%}
.why-head{font-weight:700;font-size:15px;text-align:center;padding:5px 0 4px;border-bottom:3px double var(--ink)}
.gold{color:var(--gold)}
.why-list{list-style:none;padding:6px 0 0 8px}
.why-list li{display:flex;align-items:flex-start;font-size:14.5px;line-height:16px;min-height:42px;padding-top:4px}
.why-list svg{flex:none;margin-right:9px;margin-top:-2px}

/* panels */
.panel{left:521px;width:402px;border-radius:6px;padding:9px}
.panel-head{font-weight:700;font-size:14.5px;text-align:center;padding:5px 0;border-bottom:2px solid var(--ink)}
.news{top:480px;height:183px;background:var(--gold)}
.news .frame{border:2px solid var(--ink)}
.news .panel-head{background:var(--cream);}
.news .panel-head span{color:var(--white)}
.news ul{list-style:none;padding:8px 12px 0 10px}
.news li{position:relative;padding-left:24px;color:var(--white);font-weight:700;font-size:14.5px;line-height:16px;margin-bottom:9px}
.news li::before{content:"";position:absolute;left:0;top:5px;width:8px;height:8px;border-radius:50%;background:var(--white)}
.feedback{top:676px;height:181px;background:var(--cream)}
.feedback .frame{border:2px solid var(--ink)}
.feedback .panel-head{background:var(--cream-pale)}
.quote{text-align:center;font-size:14.5px;line-height:22px;padding:8px 20px 0}
.quote .mark{font-size:26px;vertical-align:-6px;font-weight:700}
.sign{text-align:right;padding-right:26px;color:var(--gold);font-weight:700;font-size:16px;line-height:21px;margin-top:4px}
.contact{top:873px;height:183px;background:var(--grey);color:var(--white)}
.contact .frame{border:2px solid var(--ink);position:relative;background:linear-gradient(135deg,#7a7a7a,#6a6a6a 50%,#757575)}
.contact .panel-head{color:var(--ink);background:rgba(255,255,255,.08)}
.contact-row{display:flex;align-items:center;font-weight:700;font-size:16.5px;margin:16px 0 0 18px}
.contact-row svg{margin-right:22px}
.contact-brand{position:absolute;right:14px;bottom:10px;text-align:center;font-size:12px;line-height:1;color:#dcdcdc}
.contact-brand i{display:block;width:22px;height:22px;border:2px solid #dcdcdc;margin:0 auto 5px}

/* welcome */
.welcome{left:115px;top:883px;width:350px}
.welcome h2{font-size:15px;font-weight:700;text-align:center;text-decoration:underline;margin-bottom:8px}
.welcome p{font-family:Roboto,Arial,sans-serif;font-size:10.5px;line-height:21px}

/* footer */
.footer-rule{left:0;top:1067px;width:1028px;height:7px;background:var(--gold)}
.footer{left:0;top:1074px;width:1028px;height:126px;background:var(--footer);color:var(--white)}
.footer-links{position:absolute;left:120px;top:29px;font-family:Roboto,Arial,sans-serif;font-size:11px;font-weight:700;line-height:26px}
.footer-links span{margin:0 8px}
.copyright{font-size:9px;line-height:20px}
.social{position:absolute;left:780px;top:30px;display:flex;gap:6px}
.social span{display:flex;align-items:center;justify-content:center;width:38px;height:36px;border-radius:6px;background:var(--white);color:var(--ink);font-size:9px;font-weight:700}
</style>
</head>
<body>

<header class="brand abs">
  <div class="brand-mark"></div>
  <div class="brand-name">TERRA LOOP</div>
  <div class="brand-sub">RECYCLING</div>
</header>

<nav class="nav abs">
  <a class="active" href="#" style="left:68px">Home</a>
  <a href="#" style="left:170px">Start Recycling</a>
  <a href="#" style="left:306px">Scrap and Recycling</a>
  <a href="#" style="left:462px">Commercial/Industrial</a>
  <a href="#" style="left:612px">Social Rsponsibility</a>
  <a href="#" style="left:737px">Contact us</a>
</nav>

<section class="hero abs">
  <div class="hero-visual" role="img" aria-label="Photo of a steel scrap grab claw lifting over a pile of shredded metal"></div>
  <h1 class="hero-title">Saving you money,<br>Energy And<br>Resources...</h1>
</section>

<section class="steps abs">
  <svg class="abs" width="822" height="110" viewBox="0 0 822 110" style="left:0;top:0">
    <rect x="0" y="0" width="822" height="110" fill="var(--grey-light)"/>
    <polygon points="340,0 557,0 608,55 557,110 340,110 380,55" fill="var(--cream)"/>
    <polygon points="0,0 340,0 387,55 340,110 0,110" fill="var(--gold)"/>
  </svg>
  <div class="step-icon" style="left:8px;top:26px">
    <svg width="34" height="34" viewBox="0 0 34 34"><circle cx="15" cy="15" r="11" fill="none" stroke="#444" stroke-width="3"/><path d="M10 15h10M15 10v10" stroke="#444" stroke-width="2"/><path d="M23 23l8 8" stroke="#444" stroke-width="4"/></svg>
  </div>
  <div class="step-title" style="left:96px;top:11px">Select</div>
  <p class="step-text" style="left:83px;top:32px;color:#fff">Lorem Ipsum is simply dummy text of the printing and typesetting industry. Lorem Ipsum has been the industry's standard dummy text ever since the 1500s, when an unknown</p>
  <div class="step-icon" style="left:358px;top:26px">
    <svg width="26" height="30" viewBox="0 0 26 30"><rect x="1" y="1" width="24" height="28" rx="2" fill="#555"/><path d="M6 8h14M6 13h14M6 18h14M6 23h14" stroke="#fff" stroke-width="2"/></svg>
  </div>
  <div class="step-title" style="left:462px;top:11px">Details</div>
  <p class="step-text" style="left:433px;top:32px;width:135px">Lorem Ipsum is simply dummy text of the printing and typesetting industry. Lorem Ipsum has been the industry's standard dummy text</p>
  <div class="step-icon" style="left:615px;top:26px;background:#777">
    <svg width="40" height="40" viewBox="0 0 40 40"><circle cx="20" cy="14" r="8" fill="#fff"/><path d="M6 38c0-10 6-15 14-15s14 5 14 15z" fill="#fff"/></svg>
  </div>
  <div class="step-title" style="left:710px;top:11px">Contact</div>
  <p class="step-text" style="left:687px;top:32px;width:132px">Lorem Ipsum is simply dummy text of the printing and typesetting industry. Lorem Ipsum has been the industry's standard dummy text</p>
</section>

<section class="why abs">
  <div class="frame">
    <h2 class="why-head">Why <span class="gold">TERRA LOOP</span> RECYCLING?</h2>
    <ul class="why-list">
      <li><svg width="22" height="20" viewBox="0 0 22 20"><path d="M1 11l5-3 4 5 10-13 2 2-12 17z" fill="#000"/></svg>Recycling old metal products uses 95% less energy than manufacturing it from new materials.</li>
      <li><svg width="22" height="20" viewBox="0 0 22 20"><path d="M1 11l5-3 4 5 10-13 2 2-12 17z" fill="#000"/></svg>Reduces greenhouse gas emissions.</li>
      <li><svg width="22" height="20" viewBox="0 0 22 20"><path d="M1 11l5-3 4 5 10-13 2 2-12 17z" fill="#000"/></svg>Aluminum and steel can be recycled over and over again.</li>
      <li><svg width="22" height="20" viewBox="0 0 22 20"><path d="M1 11l5-3 4 5 10-13 2 2-12 17z" fill="#000"/></svg>Decreases environmental damage caused by mining.</li>
      <li><svg width="22" height="20" viewBox="0 0 22 20"><path d="M1 11l5-3 4 5 10-13 2 2-12 17z" fill="#000"/></svg>Less land and water pollution.</li>
      <li><svg width="22" height="20" viewBox="0 0 22 20"><path d="M1 11l5-3 4 5 10-13 2 2-12 17z" fill="#000"/></svg>Aluminum and steel can be recycled over and over again.</li>
      <li><svg width="22" height="20" viewBox="0 0 22 20"><path d="M1 11l5-3 4 5 10-13 2 2-12 17z" fill="#000"/></svg>Decreases environmental damage caused by mining.</li>
      <li><svg width="22" height="20" viewBox="0 0 22 20"><path d="M1 11l5-3 4 5 10-13 2 2-12 17z" fill="#000"/></svg>Less land and water pollution.</li>
    </ul>
  </div>
</section>

<section class="panel news abs">
  <div class="frame">
    <h2 class="panel-head">Latest <span>News</span></h2>
    <ul>
      <li>Lorem Ipsum is simply dummy text of the printing and typesetting industry.</li>
      <li>Lorem Ipsum is simply dummy text of the printing and typesetting industry.</li>
      <li>Lorem Ipsum is simply dummy text of the printing and typesetting industry.</li>
    </ul>
  </div>
</section>

<section class="panel feedback abs">
  <div class="frame">
    <h2 class="panel-head">Client <span class="gold">Feedback</span></h2>
    <p class="quote"><span class="mark">"</span>Quick helping hands...just what a customer wants.<br>Everyone is nice...keep it up.<br>TERRA LOOP satisfied customer always comes back.!</p>
    <p class="sign">Darren Ho<br>(Satisfied Customer)</p>
  </div>
</section>

<section class="welcome abs">
  <h2>WELCOME to <span class="gold">TERRA LOOP</span> RECYCLING</h2>
  <p>Lorem Ipsum is simply dummy text of the printing and typesetting industry. Lorem Ipsum has been the industry's standard dummy text ever since the 1500s, when an unknown printer took a galley of type and scrambled it to make a type specimen book. It has survived not only five centuries, but also the leap into electronic typesetting, remaining essentially unchanged.</p>
</section>

<section class="panel contact abs">
  <div class="frame" role="img" aria-label="Contact panel over a faint street map background">
    <h2 class="panel-head">Contact <span style="color:#fff">Us</span></h2>
    <div class="contact-row">
      <svg width="46" height="30" viewBox="0 0 46 30"><path d="M2 10c6-9 36-9 42 0l-2 5-8-2v-4H12v4l-8 2z" fill="#fff"/><path d="M12 14h22l6 14H6z" fill="#fff"/><circle cx="23" cy="21" r="4" fill="#6c6c6c"/></svg>
      1800-555-0147
    </div>
    <div class="contact-row">
      <svg width="46" height="28" viewBox="0 0 46 28"><rect x="6" y="2" width="34" height="24" fill="none" stroke="#fff" stroke-width="2.5"/><path d="M6 2l17 14 17-14M6 26l12-12M40 26L28 14" fill="none" stroke="#fff" stroke-width="2.5"/></svg>
      info@terraloop.example
    </div>
    <div class="contact-brand"><i></i>TERRA LOOP<br><small style="font-size:8px">RECYCLING</small></div>
  </div>
</section>

<div class="footer-rule abs"></div>
<footer class="footer abs">
  <div class="footer-links">
    <div>home<span>|</span>start recycling<span>|</span>scrap&amp;recycling<span>|</span></div>
    <div>commercial/industrial<span>|</span>social responsibility<span>|</span>contact us</div>
    <div class="copyright">copy-right@terraloop.example</div>
  </div>
  <div class="social">
    <span>Linkup</span><span>Clipcast</span><span>Postwave</span>
  </div>
</footer>

</body>
</html>
```